Vitamin/Dietary Supplement Company needs a simple Hemp CBD Health retail website to display a few...

We need a simple website designed that will allow us to display a few products for purchase. We are a vitamin/dietary supplement company that wants to set up a separate website for CBD health products. CBD is a chemical compound found in hemp and cannabis plants that provide various health and medicinal benefits. Our target audience are individuals that suffer from health issues and would like to treat their pain relief with CBD as an alternative to prescription medication and over the counter drugs such as Paxorin and Dolvex. Looking for a simple and clean website that is easy for customers to navigate and purchase products.

Need extra days to review

Target Market(s)

Our target audience are individuals that suffer from health issues and would like to treat their pain relief with CBD as an alternative to prescription medication and over the counter drugs such as Paxorin and Dolvex.

Coding

Coded - Design and coding required

Font styles to use
Serif

Colors

Designer to choose colors to be used in the design.

Requirements
Nice to have
• Homepage, About page, FAQ page, Contact page, Blog page

```html
<!DOCTYPE html>
<html lang="en">
<head>
<meta charset="utf-8">
<title>Verdance Relief – Hemp Extracts</title>
<link rel="stylesheet" href="https://fonts.googleapis.com/css2?family=Roboto:ital,wght@0,300;0,400;0,500;0,700;0,900;1,400;1,700&family=Roboto+Condensed:wght@700&display=swap">
<style>
:root{
  --navy:#0c2b4c;
  --navy-deep:#0a2441;
  --green:#4f9a24;
  --green-dark:#2f6d12;
  --lime:#a5cc2a;
  --pale-green:#edf5d6;
  --text:#1b2a3a;
  --muted:#8a8f96;
  --white:#ffffff;
  --star:#f2b800;
}
*{box-sizing:border-box;margin:0;padding:0}
html,body{width:1200px;height:3689px;overflow:hidden}
body{position:relative;font-family:"Roboto",sans-serif;color:var(--text);background:var(--white)}
.abs{position:absolute}
.btn{position:absolute;display:flex;align-items:center;justify-content:center;border-radius:20px;background:linear-gradient(#5aa62c,#2d6a10);color:var(--white);font-size:13px;font-weight:500}
.mark{width:30px;height:30px;border-radius:50%;background:var(--navy)}

/* header & hero */
.hero{position:absolute;left:0;top:0;width:1200px;height:563px;background:linear-gradient(90deg,#f4f8ec 0%,#eef5dc 45%,#e3edc8 100%)}
.hero-photo{position:absolute;left:470px;top:0;width:730px;height:563px;background:radial-gradient(ellipse at 60% 40%,#6a9a3a 0%,#a9c780 35%,#dfeac8 65%,rgba(238,245,220,0) 85%),linear-gradient(180deg,rgba(0,0,0,0) 70%,#b89a6a 100%)}
.logo{position:absolute;left:80px;top:42px;display:flex;align-items:center;gap:10px;font-family:"Roboto Condensed",sans-serif;font-weight:700;font-size:20px;color:var(--navy)}
.nav{position:absolute;top:78px;left:460px;display:flex;gap:0;font-size:13px;color:#3a4a5a;letter-spacing:.5px}
.nav span{position:absolute;white-space:nowrap}
.account{position:absolute;right:80px;top:38px;font-size:14px;color:var(--navy);display:flex;gap:14px;align-items:center}
.hero-title{position:absolute;left:78px;top:258px;font-size:53px;font-weight:700;color:var(--navy);letter-spacing:2px}
.hero-sub{position:absolute;left:82px;top:312px;font-size:34px;font-weight:300;color:var(--navy);letter-spacing:5px}

/* feature band */
.features{position:absolute;left:0;top:563px;width:1200px;height:327px;background:var(--navy)}
.feature{position:absolute;top:89px;width:226px;height:196px;border:2px solid var(--green);text-align:center;color:var(--white)}
.feature .icon{position:absolute;left:70px;top:-42px;width:84px;height:84px;border-radius:50%;background:var(--navy);border:2px solid var(--white);display:flex;align-items:center;justify-content:center}
.feature h3{margin-top:66px;font-size:20px;font-weight:500}
.feature p{margin:12px 18px 0;font-size:13px;line-height:20px}

/* about */
.about-title{position:absolute;left:177px;top:1036px;display:flex;align-items:center;gap:14px;font-size:26px;font-weight:700;font-style:italic;color:var(--navy)}
.about-text{position:absolute;left:177px;top:1090px;width:420px;font-size:12.5px;line-height:21px;color:var(--muted)}
.about-photo{position:absolute;left:652px;top:1029px;width:376px;height:291px;background:radial-gradient(circle at 40% 40%,#5a9a2a,#2d6a18 60%,#1e4a12)}
.about-photo span{position:absolute;left:130px;top:120px;color:var(--white);font-size:44px;font-weight:300}
.about-photo em{position:absolute;left:150px;top:170px;color:var(--white);font-style:normal;font-size:18px;font-weight:300}

/* section headings */
.sec-mark{position:absolute;left:585px}
.sec-title{position:absolute;left:0;width:1200px;text-align:center;font-size:35px;font-weight:700;color:var(--navy)}
.sec-sub{position:absolute;left:0;width:1200px;text-align:center;font-size:14px;font-style:italic;color:#3e4a56;line-height:22px;letter-spacing:.6px}

/* process */
.timeline{position:absolute;left:288px;top:1638px;width:624px;height:2px;background:#c8ced4}
.step{position:absolute;top:1618px;width:40px;height:40px;border-radius:50%;background:var(--navy);color:var(--white);display:flex;align-items:center;justify-content:center;font-size:16px}
.process{position:absolute;top:1722px;width:271px;height:191px;border:2px solid var(--green);text-align:center}
.process .glyph{position:absolute;left:112px;top:-30px;width:48px;height:48px;background:var(--white);border:2px solid var(--navy);border-radius:6px}
.process h4{margin-top:46px;font-size:17px;font-weight:500;color:var(--navy)}
.process p{margin:10px 26px 0;font-size:12.5px;line-height:19px;color:var(--muted)}
.process .btn{left:90px;bottom:10px;width:91px;height:22px;font-size:11px}

/* products */
.card{position:absolute;top:2220px;width:232px;height:306px;border:1px solid #dfe3e7;text-align:center;background:var(--white)}
.card .photo{height:197px}
.card h5{margin-top:14px;font-size:15px;font-weight:500;color:var(--navy)}
.card .price{margin-top:6px;font-size:22px;color:var(--navy)}
.card .stars{margin-top:0;font-size:12px;color:var(--star);letter-spacing:1px}
.card .btn{left:70px;bottom:6px;width:92px;height:22px;font-size:11px}

/* benefits */
.benefits{position:absolute;left:0;top:2590px;width:1200px;height:607px;background:var(--pale-green)}
.plant{position:absolute;left:440px;top:165px;width:320px;height:417px;background:radial-gradient(ellipse at 50% 28%,#7fba3a 0%,rgba(127,186,58,.4) 30%,rgba(237,245,214,0) 55%),radial-gradient(ellipse at 50% 90%,#3a2a1e 0%,#5a4230 28%,rgba(237,245,214,0) 52%)}
.point{position:absolute;font-size:15px;font-weight:500;line-height:22px;color:var(--navy)}
.point.left{left:144px;border-left:4px solid var(--navy);padding-left:18px;width:300px}
.point.right{right:144px;border-right:4px solid var(--navy);padding-right:18px;width:300px;text-align:right}
.point.accent{border-color:var(--lime)}

/* newsletter */
.newsletter{position:absolute;left:0;top:3197px;width:1200px;height:165px;background:var(--lime)}
.newsletter h2{position:absolute;left:182px;top:45px;font-size:26px;font-weight:700;font-style:italic;color:var(--navy)}
.newsletter p{position:absolute;left:182px;top:80px;font-size:22px;font-style:italic;color:var(--white);line-height:28px}
.newsletter .field{position:absolute;left:745px;top:62px;width:230px;height:42px;border-radius:21px 0 0 21px;background:var(--white);font-size:13px;color:#9aa0a6;padding:13px 0 0 26px}
.newsletter .send{position:absolute;left:935px;top:62px;width:122px;height:42px;border-radius:21px;background:var(--navy);color:var(--white);font-size:13px;display:flex;align-items:center;justify-content:center}

/* footer */
.footer{position:absolute;left:0;top:3362px;width:1200px;height:327px;background:var(--navy);color:var(--white)}
.footer .brand{position:absolute;left:88px;top:60px;display:flex;align-items:center;gap:12px;font-size:30px;font-weight:400}
.footer .about{position:absolute;left:82px;top:176px;width:210px;font-size:13px;line-height:23px}
.footer h6{position:absolute;top:45px;font-size:15px;font-weight:500;color:var(--lime)}
.footer ul{position:absolute;top:86px;list-style:none;font-size:14px;line-height:33px}
.contact{position:absolute;font-size:13px;line-height:20px;display:flex;gap:12px}
.input{position:absolute;left:925px;width:195px;height:33px;border:1px solid #c4ccd4;border-radius:3px;font-size:10px;color:#c4ccd4;padding:9px 10px}
.footer .go{position:absolute;left:925px;top:216px;width:92px;height:32px;border-radius:16px;background:var(--lime);color:var(--navy);font-size:12px;display:flex;align-items:center;justify-content:center}
.footer .rule{position:absolute;left:0;top:253px;width:1200px;height:1px;background:#4a6480}
.footer .copy{position:absolute;left:0;top:268px;width:1200px;text-align:center;font-size:11px}
</style>
</head>
<body>

<header class="hero">
  <div class="hero-photo" role="img" aria-label="Photo of a glass jar of golden hemp oil beside a fresh hemp plant on a wooden stump"></div>
  <div class="logo"><span class="mark"></span>Verdance Relief</div>
  <nav class="nav">
    <span style="left:0">HOME</span>
    <span style="left:98px">WHAT IS CBD</span>
    <span style="left:288px">EDUCATION</span>
    <span style="left:466px">PRODUCTS</span>
    <span style="left:597px">BENEFITS</span>
  </nav>
  <div class="account"><span><b>Login</b>/Register</span>
    <svg width="20" height="18" viewBox="0 0 24 22"><path d="M1 2h4l3 12h12l3-9H7" fill="none" stroke="#0c2b4c" stroke-width="2.4"/><circle cx="10" cy="19" r="2" fill="#0c2b4c"/><circle cx="19" cy="19" r="2" fill="#0c2b4c"/></svg></div>
  <h1 class="hero-title">Hemp Extracts</h1>
  <div class="hero-sub">crafted with care</div>
  <div class="btn" style="left:81px;top:370px;width:160px;height:36px;justify-content:flex-start;padding-left:14px;gap:20px">
    <svg width="18" height="16" viewBox="0 0 24 22"><path d="M1 2h4l3 12h12l3-9H7" fill="none" stroke="#fff" stroke-width="2.4"/><circle cx="10" cy="19" r="2" fill="#fff"/><circle cx="19" cy="19" r="2" fill="#fff"/></svg>SHOP NOW</div>
</header>

<section class="features">
  <div class="feature" style="left:96px">
    <div class="icon"><svg width="40" height="36" viewBox="0 0 24 22"><path d="M1 2h4l3 12h12l3-9H7" fill="none" stroke="#fff" stroke-width="1.8"/><circle cx="10" cy="19" r="1.8" fill="#fff"/><circle cx="19" cy="19" r="1.8" fill="#fff"/></svg></div>
    <h3>SHOP CBD</h3><p>CBD Oil, derived from agricultural hemp, been widely recognized for many benefits</p>
  </div>
  <div class="feature" style="left:359px">
    <div class="icon"><svg width="44" height="44" viewBox="0 0 24 24"><circle cx="12" cy="12" r="11" fill="#fff"/><circle cx="12" cy="6.5" r="1.6" fill="#0c2b4c"/><path d="M10 10h3v8h1.5v1.5h-5V18H11v-6.5h-1z" fill="#0c2b4c"/></svg></div>
    <h3>WHAT IS CBD?</h3><p>CBD Oil, derived from agricultural hemp, been widely recognized for many benefits</p>
  </div>
  <div class="feature" style="left:622px">
    <div class="icon"><svg width="46" height="32" viewBox="0 0 30 20"><circle cx="15" cy="5" r="4" fill="#fff"/><path d="M8 19c0-5 3-8 7-8s7 3 7 8z" fill="#fff"/><circle cx="6" cy="7" r="3" fill="#fff"/><path d="M0 18c0-4 2-6 6-6 1 0 2 .3 2.5.6C7.5 14 7 16 7 18z" fill="#fff"/><circle cx="24" cy="7" r="3" fill="#fff"/><path d="M30 18c0-4-2-6-6-6-1 0-2 .3-2.5.6 1 1.4 1.5 3.4 1.5 5.4z" fill="#fff"/></svg></div>
    <h3>BENEFITS OF CBD</h3><p>CBD Oil, derived from agricultural hemp, been widely recognized for many benefits</p>
  </div>
  <div class="feature" style="left:888px">
    <div class="icon"><svg width="44" height="44" viewBox="0 0 24 24"><circle cx="12" cy="12" r="11" fill="#fff"/><text x="12" y="17" text-anchor="middle" font-family="Roboto,sans-serif" font-weight="700" font-size="15" fill="#0c2b4c">$</text></svg></div>
    <h3>DEALS ON CBD</h3><p>CBD Oil, derived from agricultural hemp, been widely recognized for many benefits</p>
  </div>
</section>

<section>
  <h2 class="about-title"><span class="mark" style="width:26px;height:26px"></span>What is CBD?</h2>
  <p class="about-text">CBD Oil, derived from agricultural hemp, has been widely recognized for many benefits on human health. It has grown in popularity amongst the medical community as a key supplement for maintaining homeostasis. Because CBD oil has the ability to talk to nearly every organ system in the body</p>
  <div class="btn" style="left:177px;top:1240px;width:122px;height:30px">Learn More</div>
  <div class="about-photo" role="img" aria-label="Close-up photo of green cannabis leaves with a molecule outline"><span>CBD</span><em>cannabinoids</em></div>
</section>

<section>
  <div class="sec-mark mark" style="top:1450px"></div>
  <h2 class="sec-title" style="top:1497px">HOW WE DO IT</h2>
  <p class="sec-sub" style="top:1553px">Our strict sourcing and business practices are designed to have minimal negative impact on the<br>environment, while the products themselves are of the utmost highest quality.</p>
  <div class="timeline"></div>
  <div class="step" style="left:268px">1</div>
  <div class="step" style="left:580px">2</div>
  <div class="step" style="left:892px">3</div>
  <div class="process" style="left:152px"><div class="glyph" role="img" aria-label="Farming icon"></div><h4>FARMING</h4><p>Our hemp is bred specifically for high terpene and cannabinoid contents. We've partnered</p><div class="btn">Read More</div></div>
  <div class="process" style="left:465px"><div class="glyph" role="img" aria-label="Extraction icon"></div><h4>EXTRACTION</h4><p>The flowers are run through enviromentally friendly alcohol extraction systems. Some of our products.</p><div class="btn">Read More</div></div>
  <div class="process" style="left:777px"><div class="glyph" role="img" aria-label="Manufacturing icon"></div><h4>MANUFACTURING</h4><p>Greenfield's final products are made in accordance with Current Good Manufacturing Practices (CGMPs)</p><div class="btn">Read More</div></div>
</section>

<section>
  <div class="sec-mark mark" style="top:2030px"></div>
  <h2 class="sec-title" style="top:2084px">LATEST HEMP PRODUCTS</h2>
  <p class="sec-sub" style="top:2132px">Nova Rx has quality CBD Hemp Oil for sale online. Cannabidiol, also known as CBD,<br>is an organic compound that is extracted from the hemp plant.</p>
  <div class="card" style="left:116px"><div class="photo" role="img" aria-label="Photo of hemp oil dropper bottles on hemp leaves" style="background:linear-gradient(160deg,#e7d9b8,#8a5a2a 55%,#4a7a2a)"></div><h5>HEMP SPEAR MINT OIL</h5><div class="price">$ 22</div><div class="stars">★★★★★</div><div class="btn">Shop Now</div></div>
  <div class="card" style="left:361px"><div class="photo" role="img" aria-label="Photo of green hemp skincare tubes and bottles" style="background:linear-gradient(160deg,#1a1a1a,#6aa83a 55%,#dfe8cf)"></div><h5>HEMP SPEAR MINT OIL</h5><div class="price">$ 22</div><div class="stars">★★★★★</div><div class="btn">Shop Now</div></div>
  <div class="card" style="left:607px"><div class="photo" role="img" aria-label="Photo of hemp oil dropper bottles on hemp leaves" style="background:linear-gradient(160deg,#e7d9b8,#8a5a2a 55%,#4a7a2a)"></div><h5>HEMP SPEAR MINT OIL</h5><div class="price">$ 22</div><div class="stars">★★★★★</div><div class="btn">Shop Now</div></div>
  <div class="card" style="left:853px"><div class="photo" role="img" aria-label="Photo of pastel hemp body moisturizer pump bottles" style="background:linear-gradient(160deg,#f3dccf,#e7b9a6 40%,#e9e4a8 70%,#b7895a)"></div><h5>HEMP BODY MOISTURE</h5><div class="price">$ 22</div><div class="stars">★★★★★</div><div class="btn">Shop Now</div></div>
</section>

<section class="benefits">
  <div class="sec-mark mark" style="top:30px"></div>
  <h2 class="sec-title" style="top:80px">THE BENEFITS OF CANNABIS</h2>
  <p class="sec-sub" style="top:134px">All of our ingestible and vape products are analyzed by third party laboratories</p>
  <div class="plant" role="img" aria-label="Illustration of a young hemp plant growing from a mound of soil"></div>
  <div class="point left" style="top:330px">Hemp and marijuana are both forms of cannabis</div>
  <div class="point left accent" style="top:400px">Cannabis rich in THC (what makes people high) is marijuana</div>
  <div class="point left" style="top:470px">Cannabis with low THC is called hemp</div>
  <div class="point right" style="top:330px">Both have many health-promoting compounds</div>
  <div class="point right accent" style="top:400px">Greenfield's products are made from hemp</div>
  <div class="point right" style="top:470px">Stay healthy without getting high</div>
</section>

<section class="newsletter">
  <span class="mark abs" style="left:142px;top:40px;width:28px;height:28px"></span>
  <h2>SUBSCRIBE TOOUR NEWSLETTER</h2>
  <p>Join our mailing list and save<br>10% off 1st order!</p>
  <div class="field">Enter email.........</div>
  <div class="send">SUBSCRIBE</div>
</section>

<footer class="footer">
  <div class="brand"><span class="mark" style="background:#fff;width:34px;height:34px"></span>Verdance Relief</div>
  <p class="about">CBD Oil, derived from agricultural hemp, has been widely recognized fo 0 many benefits on human health.</p>
  <h6 style="left:413px">NAVIGATION</h6>
  <ul style="left:413px"><li>Home</li><li>What is CBD</li><li>Education</li><li>Products</li><li>Benefits</li></ul>
  <h6 style="left:652px">CONTACT INFO</h6>
  <div class="contact" style="left:652px;top:86px"><svg width="14" height="18" viewBox="0 0 14 20"><path d="M7 0a7 7 0 0 0-7 7c0 5 7 13 7 13s7-8 7-13a7 7 0 0 0-7-7z" fill="#fff"/><circle cx="7" cy="7" r="2.5" fill="#0c2b4c"/></svg><span>CBD Oil, derived fro<br>agricultural hemp, has</span></div>
  <div class="contact" style="left:652px;top:140px"><svg width="12" height="18" viewBox="0 0 12 20"><rect x="1" y="1" width="10" height="18" rx="2" fill="none" stroke="#fff" stroke-width="2"/><circle cx="6" cy="16" r="1" fill="#fff"/></svg><span>xxxxxxxxxx</span></div>
  <h6 style="left:925px">GET IN TOUCH</h6>
  <div class="input" style="top:76px">Name</div>
  <div class="input" style="top:114px">Email</div>
  <div class="input" style="top:152px;height:44px">Message</div>
  <div class="go">SEND</div>
  <div class="rule"></div>
  <div class="copy">© ALL RIGHT RESERVERD!</div>
</footer>

</body>
</html>
```